Corvane Holdings , new business card design

investment firm with corporate clients . need double sided business card , vertical and horizontal options ,logo must be clear. prefer pantone colors only and sharp design. website also www.corvane-example.ae

Khalid Bin Rashed
Managing Director
Tel. +971 4 000 3829
Mobile +971 50 000 4172
khalid@corvane-example.ae
Palm Crest Tower, officw 18-B07, Qasr Gardens, Dubai

Contact Information for Business Card

Khalid Bin Rashed
Managing Director

Font styles to use
Serif

Colors

Designer to choose colors to be used in the design.

```html
<!DOCTYPE html>
<html lang="en">
<head>
<meta charset="utf-8">
<title>Corvane Holdings – Business Card</title>
<link rel="stylesheet" href="https://fonts.googleapis.com/css2?family=Roboto:wght@300;400;500&family=Roboto+Condensed:wght@700&display=swap">
<style>
  :root {
    --backdrop: #7a5540;
    --card-white: #f4f4f3;
    --brand-blue: #48729a;
    --ink: #1e1e1e;
    --ink-soft: #555a60;
    --white: #ffffff;
  }
  * { margin: 0; padding: 0; box-sizing: border-box; }
  html, body { width: 1200px; height: 960px; overflow: hidden; }
  body {
    position: relative;
    background: var(--backdrop);
    font-family: "Roboto", Arial, sans-serif;
  }
  .card {
    position: absolute;
    width: 600px;
    height: 343px;
    box-shadow: 0 2px 6px rgba(0,0,0,0.35);
  }
  .card--front { left: 152px; top: 125px; background: var(--card-white); }
  .card--back { left: 452px; top: 500px; background: var(--brand-blue); }

  .edge-bar {
    position: absolute;
    left: 169px;
    width: 261px;
    height: 5px;
    background: var(--brand-blue);
  }
  .edge-bar--top { top: 0; }
  .edge-bar--bottom { bottom: 0; }

  .wordmark {
    position: absolute;
    font-family: "Roboto", Arial, sans-serif;
    font-weight: 300;
    text-transform: uppercase;
    line-height: 1;
  }
  .wordmark__main { display: block; font-size: 38px; letter-spacing: 0.32em; }
  .wordmark__sub { display: block; font-size: 13px; letter-spacing: 0.98em; margin-top: 6px; }
  .card--front .wordmark { left: 46px; top: 146px; color: var(--ink); }
  .card--back .wordmark { left: 0; width: 600px; top: 144px; text-align: center; color: var(--white); }
  .card--back .wordmark__main, .card--back .wordmark__sub { margin-right: -0.32em; }

  .holder {
    position: absolute;
    left: 330px;
    top: 81px;
    padding-left: 17px;
    border-left: 5px solid var(--brand-blue);
  }
  .holder__name {
    font-family: "Roboto Condensed", "Arial Narrow", sans-serif;
    font-weight: 700;
    font-size: 19px;
    color: var(--brand-blue);
    text-transform: uppercase;
    line-height: 22px;
  }
  .holder__title {
    font-weight: 500;
    font-size: 14.5px;
    color: var(--ink);
    text-transform: uppercase;
    line-height: 18px;
  }
  .address {
    position: absolute;
    left: 329px;
    top: 140px;
    font-size: 14px;
    line-height: 19.5px;
    color: var(--ink-soft);
    font-style: normal;
  }
  .contacts {
    position: absolute;
    left: 329px;
    top: 193px;
    list-style: none;
    font-size: 14px;
    color: var(--ink-soft);
  }
  .contacts li {
    display: flex;
    align-items: center;
    height: 19px;
  }
  .contacts svg { width: 13px; height: 13px; margin-right: 8px; fill: var(--brand-blue); flex: none; }

  .back-url {
    position: absolute;
    left: 0;
    width: 600px;
    top: 288px;
    text-align: center;
    color: var(--white);
    font-size: 15px;
    letter-spacing: 0.36em;
    margin-right: -0.36em;
  }
</style>
</head>
<body>

<section class="card card--front" aria-label="Business card front">
  <span class="edge-bar edge-bar--top"></span>
  <span class="edge-bar edge-bar--bottom"></span>

  <div class="wordmark">
    <span class="wordmark__main">Corvane</span>
    <span class="wordmark__sub">Holdings</span>
  </div>

  <div class="holder">
    <p class="holder__name">Khalid Bin Rashed</p>
    <p class="holder__title">Managing Director</p>
  </div>

  <address class="address">
    Palm Crest Tower, officw 18-B07<br>
    Qasr Gardens, Dubai
  </address>

  <ul class="contacts">
    <li>
      <svg viewBox="0 0 16 16" aria-hidden="true"><path d="M3.6 1.2l2.3 2.6c.4.4.4 1 0 1.4L4.8 6.4c.9 2 2.6 3.8 4.7 4.8l1.2-1.2c.4-.4 1-.4 1.4 0l2.6 2.3c.4.4.4 1 0 1.4l-1.3 1.3C11.3 16.1 0 6.9 1 2.6L2.2 1.2c.4-.4 1-.4 1.4 0z"/></svg>
      +971 4 000 3829
    </li>
    <li>
      <svg viewBox="0 0 16 16" aria-hidden="true"><path d="M4.5 0h7c.8 0 1.5.7 1.5 1.5v13c0 .8-.7 1.5-1.5 1.5h-7C3.7 16 3 15.3 3 14.5v-13C3 .7 3.7 0 4.5 0zM4.6 2v10.5h6.8V2zM8 13.3a.9.9 0 100 1.8.9.9 0 000-1.8z"/></svg>
      +971 50 000 4172
    </li>
    <li>
      <svg viewBox="0 0 16 16" aria-hidden="true"><path d="M1 3.5h14v1L8 9 1 4.5zM1 6l7 4.5L15 6v6.5H1z"/></svg>
      khalid@corvane-example.ae
    </li>
    <li>
      <svg viewBox="0 0 16 16" aria-hidden="true"><circle cx="8" cy="8" r="7"/><path d="M5 4.5c1 .3 1.6 1 1.4 2-.2.8-1.3 1-1.2 2 .1.8 1 1.2 1 2.3L5.5 13M10 2.5c-.5 1 .3 1.6 1.2 1.8 1 .2 1.3 1 .8 1.8-.4.8-1.6.6-1.8 1.6-.2.9.8 1.6.3 2.8" fill="none" stroke="#f4f4f3" stroke-width="1.1"/></svg>
      www.corvane-example.ae
    </li>
  </ul>
</section>

<section class="card card--back" aria-label="Business card back">
  <div class="wordmark">
    <span class="wordmark__main">Corvane</span>
    <span class="wordmark__sub">Holdings</span>
  </div>
  <p class="back-url">www.corvane-example.ae</p>
</section>

</body>
</html>
```